Coffee and fruit juice

We are a malaysian restaurant that also serves aussie coffee and breakfast from 7am to 11am. After 11am we serve malaysian food but we also have a salad and sandwhich bar for people to choose from. We need a poster to hang outside our door to let people know that we are now also serving aussie coffee and breakfast as well as our usual malaysian cuisine.

Target Market(s)

Office location

Industry/Entity Type

Restaurant

Font styles to use
Decorative
Script

Requirements
Must have
• images and word
Nice to have
• something bold to attract people's attention

```html
<!DOCTYPE html>
<html lang="en">
<head>
<meta charset="utf-8">
<title>Malaysian Food — Coffee and Breakfast Poster</title>
<link href="https://fonts.googleapis.com/css2?family=Lobster&display=swap" rel="stylesheet">
<style>
  :root {
    --charcoal-dark: #1c1c1c;
    --charcoal-mid: #4a4a4a;
    --charcoal-light: #7a7a7a;
    --orange: #c85e0c;
    --orange-bright: #f07a10;
    --orange-deep: #9c4506;
    --ink: #111111;
    --white: #ffffff;
    --ring: #3a3a3a;
  }
  html, body {
    margin: 0;
    padding: 0;
    width: 900px;
    height: 1200px;
    overflow: hidden;
    background: #f2f2f2;
  }
  .poster {
    position: relative;
    width: 900px;
    height: 1200px;
    overflow: hidden;
    background: radial-gradient(circle at 40% 35%, var(--charcoal-light) 0%, var(--charcoal-mid) 40%, var(--charcoal-dark) 100%);
    font-family: "Lobster", cursive;
  }
  .hero-dish {
    position: absolute;
    left: -40px;
    top: 20px;
    width: 560px;
    height: 540px;
    border-radius: 50%;
    background: radial-gradient(circle at 50% 45%, #e8b15a 0%, #a8542a 45%, #6d3a1c 75%, #3e2612 100%);
    box-shadow: 0 12px 30px rgba(0,0,0,0.55);
  }
  .serve-ribbon {
    position: absolute;
    left: 590px;
    top: -10px;
    width: 250px;
    height: 400px;
  }
  .serve-ribbon-text {
    position: absolute;
    left: 590px;
    top: 45px;
    width: 250px;
    text-align: center;
    font-size: 58px;
    line-height: 1.22;
    color: var(--ink);
  }
  .serve-ribbon-text .time { color: var(--white); }
  .cuisine-title {
    position: absolute;
    right: 48px;
    top: 385px;
    text-align: right;
  }
  .cuisine-title .region {
    display: block;
    font-size: 60px;
    color: var(--white);
    line-height: 1;
    text-shadow: 0 3px 6px rgba(0,0,0,0.6);
  }
  .cuisine-title .dish {
    display: block;
    font-size: 124px;
    color: var(--orange-bright);
    line-height: 1.05;
    text-shadow: 0 4px 8px rgba(0,0,0,0.6);
  }
  .breakfast-band {
    position: absolute;
    left: 0;
    top: 620px;
    width: 900px;
    height: 540px;
  }
  .menu-photo {
    position: absolute;
    width: 230px;
    height: 230px;
    border-radius: 50%;
    border: 8px solid var(--white);
    box-shadow: 0 0 0 6px var(--ring), 0 8px 16px rgba(0,0,0,0.5);
  }
  .menu-photo.coffee {
    left: 55px;
    top: 662px;
    background: radial-gradient(circle at 40% 45%, #8a5a3c 0%, #d9c3a8 40%, #f4ede4 75%);
  }
  .menu-photo.sandwich {
    left: 45px;
    top: 904px;
    background: radial-gradient(circle at 45% 50%, #d99a52 0%, #c9a574 40%, #ede6da 80%);
  }
  .breakfast-title {
    position: absolute;
    left: 350px;
    top: 715px;
    font-size: 96px;
    line-height: 1.12;
    color: var(--ink);
    margin: 0;
    font-weight: 400;
  }
  .breakfast-hours {
    position: absolute;
    left: 352px;
    top: 965px;
    font-size: 66px;
    color: var(--white);
    margin: 0;
  }
</style>
</head>
<body>
<main class="poster">
  <div class="hero-dish" role="img" aria-label="Photo of grilled satay skewers on a banana leaf with rice cakes and peanut sauce"></div>

  <svg class="serve-ribbon" viewBox="0 0 250 400" aria-hidden="true">
    <defs>
      <radialGradient id="ribbonFill" cx="50%" cy="40%" r="70%">
        <stop offset="0%" stop-color="#e07012"/>
        <stop offset="100%" stop-color="#9c4506"/>
      </radialGradient>
    </defs>
    <polygon points="4,0 246,0 246,310 125,392 4,310" fill="url(#ribbonFill)" stroke="#ffffff" stroke-width="7"/>
  </svg>
  <div class="serve-ribbon-text">Serve<br>After<br><span class="time">11am</span></div>

  <h1 class="cuisine-title">
    <span class="region">Malaysian</span>
    <span class="dish">Food</span>
  </h1>

  <svg class="breakfast-band" viewBox="0 620 900 540" aria-hidden="true">
    <defs>
      <radialGradient id="bandFill" cx="55%" cy="40%" r="70%">
        <stop offset="0%" stop-color="#e07012"/>
        <stop offset="100%" stop-color="#8f3f05"/>
      </radialGradient>
    </defs>
    <polygon fill="url(#bandFill)" stroke="#ffffff" stroke-width="4" stroke-linejoin="round"
      points="-5,646 30,640 60,650 90,643 120,652 150,641 180,648 210,655 240,644 270,650 300,639 330,649 360,645 390,653 420,642 450,650 480,646 510,638 540,651 570,644 600,649 630,641 660,654 690,645 720,648 750,640 780,650 810,643 840,652 870,646 905,644
              905,1136 870,1130 840,1140 810,1132 780,1141 750,1129 720,1137 690,1144 660,1133 630,1139 600,1128 570,1138 540,1134 510,1142 480,1131 450,1139 420,1135 390,1127 360,1140 330,1133 300,1138 270,1130 240,1143 210,1134 180,1137 150,1129 120,1139 90,1132 60,1141 30,1135 -5,1133"/>
  </svg>

  <div class="menu-photo coffee" role="img" aria-label="Photo of a cup of coffee with chocolate pieces"></div>
  <div class="menu-photo sandwich" role="img" aria-label="Photo of a toasted chicken and salad sandwich"></div>

  <h2 class="breakfast-title">Coffee and<br>Breakfast</h2>
  <p class="breakfast-hours">7am to 11am</p>
</main>
</body>
</html>
```